Velto Works CBD Packaging Label Design. Creative Modern Minimalist. Future Work possible!!!

Creating a CBD product.Bottle size is height 84mm diameter 25mmLabel size 74mm x 38mmMatch Stick Box: 40mm x 100mm x 50mm
Pippette cap is red FYI.
NOTE: We have added a logo file but I am also paying for a new logo design. So do as you please.Need the packaging and labelling done for CBD product. Name is Velto Works. Logo is included in file below. I have also added some product packaging and design for inspiration. No need to use this but to give you an idea. Some flexibility with label dimensions. In so far as, it must fit on the base of the bottle, think eye dropper.

The last brimloft cbd oil dropper is a cool industrial design but we would prefer a design with a label.Red and white are the main colors. Minimalist, modern, clean, swiss cross in the mix are acceptable.

Also, the logo image with the textured background on the business card is part of then look we would like to package. Not a requirement but certainly a consideration.Feel free to reach out for any further questions.Below are some specs and text we need to squeeze on then packaging / labelling.

The location of the text or emphasis is NOT fixed even if it specifies the location in the description below.

Box must contain:
logo, velto Works text
Warnings-(warning sign with exclamation mark) not suitable for consumption -under 18 restricted sign?
PACKAGING TEXT (Classic rectangular)
LogoCanna Labs (below logo)10% CBD Oil (x milligram mg)10ml
Disclaimers (From dorvexi)
MEDICAL: (From dorvexi website) Disclaimer: Velto Works products are sold without any medical claims; they have not been proven to treat, relieve, nor cure any disease or medical condition. please refer to the terms and conditions (need to read these from)
CONTACT: Avoid contact during pregnancy and while nursing. Do not get in eyes, on skin, or on clothing. Get medical advice/attention if you feel unwell.ADVICE: Keep out of reach of children. Protect from sunlight. Store in a well-ventilated place. Keep cool. Refrigerate after opening.
Ingredients: Ingredients: 80% MCT oil, 20% Carmagnola Selezionata (What terpenes?check with clear horizon). 100% organic. (Check labeling) Extracted using ethanol extraction.

Side note: More information about boxing size and bottle can be seen on a competitiors site. shown below.

https://dorvexi.example/product-category/selection/

Target Market(s)

CBD oil users in Europe

Logo Text

velto works

Font styles to use
Serif
Sans Serif
Script

Requirements
Must have
• I want textured, like business card texture considered for the label. The box is a standard cardboard for the moment. Pharma grade product. I would like it to stand out in a pharmacy but not look out of place.
• We need all sides of the packaging. Use lorem ipsum if you have to. Some of the text is above though
Should not have
• Nothing that references the weed leaf. Keep that off

```html
<!DOCTYPE html>
<html lang="en">
<head>
<meta charset="UTF-8">
<title>Velto Works – 10% CBD Oil Packaging</title>
<link href="https://fonts.googleapis.com/css2?family=Poppins:wght@300;400;600&display=swap" rel="stylesheet">
<style>
  :root {
    --bg: #e9e9e9;
    --paper: #f7f7f7;
    --paper-side: #efefef;
    --red: #e8333b;
    --ink: #2a2a2a;
    --muted: #555;
    --edge: #d6d6d6;
  }
  * { margin: 0; padding: 0; box-sizing: border-box; }
  html, body { width: 1200px; height: 900px; overflow: hidden; }
  body {
    background: var(--bg);
    font-family: "Poppins", sans-serif;
    color: var(--ink);
    position: relative;
  }

  /* ---------- box ---------- */
  .box {
    position: absolute;
    left: 180px;
    top: 110px;
    display: flex;
    height: 680px;
  }
  .box-side {
    width: 150px;
    height: 100%;
    background: var(--paper-side);
    border: 1px solid var(--edge);
    border-right: none;
    position: relative;
  }
  .box-side .brand-mark {
    position: absolute;
    top: 120px;
    left: 0;
    width: 100%;
    display: flex;
    flex-direction: column;
    align-items: center;
    gap: 8px;
  }
  .box-side .brand-name { font-size: 19px; }
  .box-side .disclaimer {
    position: absolute;
    left: 22px;
    bottom: 60px;
    width: 420px;
    transform-origin: left bottom;
    transform: rotate(-90deg) translateY(100%);
    font-size: 9.5px;
    line-height: 1.55;
    color: var(--muted);
    letter-spacing: 0.3px;
  }
  .box-front {
    width: 300px;
    height: 100%;
    background: var(--paper);
    border: 1px solid var(--edge);
    position: relative;
    text-align: center;
  }
  .box-front .brand-mark {
    margin-top: 86px;
    display: flex;
    flex-direction: column;
    align-items: center;
    gap: 12px;
  }
  .box-front .brand-name { font-size: 36px; }
  .box-front .rule {
    width: 220px;
    height: 4px;
    background: var(--red);
    margin: 16px auto 0;
  }
  .box-front .product {
    margin-top: 34px;
    font-size: 30px;
    font-weight: 600;
    letter-spacing: -0.5px;
  }
  .box-front .volume {
    position: absolute;
    bottom: 100px;
    width: 100%;
    font-size: 24px;
    font-weight: 600;
  }

  /* ---------- shared brand mark ---------- */
  .brand-dot {
    border: 2px solid var(--red);
    border-radius: 50%;
  }
  .brand-name {
    color: var(--red);
    font-weight: 300;
    letter-spacing: 0.5px;
    white-space: nowrap;
  }

  /* ---------- bottle label ---------- */
  .label {
    position: absolute;
    left: 760px;
    top: 280px;
    width: 280px;
    height: 340px;
    background: var(--paper);
    border: 1px solid var(--edge);
    text-align: center;
  }
  .label .brand-mark {
    margin-top: 34px;
    display: flex;
    flex-direction: column;
    align-items: center;
    gap: 8px;
    width: 200px;
  }
  .label .brand-name { font-size: 28px; }
  .label .rule {
    width: 166px;
    height: 3px;
    background: var(--red);
    margin: 12px 0 0 16px;
  }
  .label .product {
    width: 200px;
    margin-top: 30px;
    font-size: 18px;
    font-weight: 600;
  }
  .label .volume {
    position: absolute;
    left: 0;
    bottom: 26px;
    width: 200px;
    font-size: 13px;
    font-weight: 600;
  }
  .label .divider {
    position: absolute;
    left: 222px;
    top: 44px;
    width: 1.5px;
    height: 280px;
    background: var(--red);
  }
  .label .age-warning {
    position: absolute;
    left: 240px;
    top: 316px;
    transform-origin: left top;
    transform: rotate(-90deg);
    display: flex;
    align-items: center;
    gap: 6px;
    font-size: 9px;
    white-space: nowrap;
    color: var(--ink);
  }
  .age-warning svg { transform: rotate(90deg); }
</style>
</head>
<body>

  <section class="box" aria-label="Velto Works carton, side and front panels">
    <div class="box-side">
      <div class="brand-mark">
        <span class="brand-dot" style="width:24px;height:24px"></span>
        <span class="brand-name">Velto Works</span>
      </div>
      <p class="disclaimer">MEDICAL: Velto Works products are sold without any medical claims; they have not been proven to treat, relieve, nor cure any disease or medical condition.<br>CONTACT: Avoid contact during pregnancy and while nursing. Do not get in eyes, on skin, or on clothing.</p>
    </div>
    <div class="box-front">
      <div class="brand-mark">
        <span class="brand-dot" style="width:48px;height:48px"></span>
        <span class="brand-name">Velto Works</span>
      </div>
      <div class="rule"></div>
      <p class="product">10% CBD OIL</p>
      <p class="volume">10 ml</p>
    </div>
  </section>

  <section class="label" aria-label="Velto Works bottle label">
    <div class="brand-mark">
      <span class="brand-dot" style="width:34px;height:34px"></span>
      <span class="brand-name">Velto Works</span>
    </div>
    <div class="rule"></div>
    <p class="product">10% CBD OIL</p>
    <p class="volume">10 ml</p>
    <div class="divider"></div>
    <div class="age-warning">
      <svg width="16" height="16" viewBox="0 0 16 16" aria-hidden="true">
        <circle cx="8" cy="8" r="6.5" fill="none" stroke="var(--red)" stroke-width="1.5"/>
        <line x1="3.5" y1="12.5" x2="12.5" y2="3.5" stroke="var(--red)" stroke-width="1.5"/>
      </svg>
      <span>NOT SUITABLE FOR CONSUMPTION -UNDER 18</span>
    </div>
  </section>

</body>
</html>
```